依頼詳細
値段は入れず、『不安を安心に』『疑問を納得へ』『生活保護のご葬儀 自己負担0円』と言った文言を入れていただきたいです。
葬儀の流れの図も入れていただきたいです。
※添付ファイルを参照ください。
記載項目
電話番号のところは◯にしておいてください
サイズ
A4
ページ数
片面
希望イメージ
シンプル 複雑
単色 カラフル
暗い 明るい
日常 高級
遊び心 厳粛
未来的 伝統的
女性的 男性的
希望する色
赤系
納品ファイル
• 高解像度JPG (.jpg)
• イラストレーター形式 (.ai)
• フォトショップ形式 (.psd)
• PNG形式 (.png)
補足説明
■ 選んだ理由

シンプルで中身がわかりやすく気に入りました

■ 提案者全員のお礼・コメント

ありがとうございます!!また機会がありましたらお願い致します

```html
<!DOCTYPE html>
<html lang="ja">
<head>
<meta charset="utf-8">
<title>生活保護のご葬儀</title>
<link rel="stylesheet" href="https://fonts.googleapis.com/css2?family=M+PLUS+Rounded+1c:wght@500;800&family=Noto+Sans+JP:wght@400;500;700&display=swap">
<style>
:root{
  --pink:#e0407f;
  --pink-soft:#f4b6cd;
  --pink-pale:#fbe6ee;
  --rose:#d9306f;
  --ink:#555;
  --paper:#fff;
}
*{margin:0;padding:0;box-sizing:border-box}
html,body{width:849px;height:1200px;overflow:hidden;background:var(--paper)}
body{font-family:"Noto Sans JP",sans-serif;color:var(--ink);position:relative}
.blossom{position:absolute;right:0;top:0;width:440px;height:280px;
  background:radial-gradient(circle at 65% 40%,#f7c6d6 0,#f9dbe5 30%,#fdf1f5 60%,rgba(255,255,255,0) 85%);}
.title{position:absolute;left:70px;top:52px;font-family:"M PLUS Rounded 1c",sans-serif;font-weight:800;
  font-size:44px;color:var(--rose);letter-spacing:1px}
.title small{font-size:32px}
.flow-label{position:absolute;left:8px;top:128px;width:36px;height:92px;background:var(--pink);color:#fff;
  writing-mode:vertical-rl;font-weight:700;font-size:22px;display:flex;align-items:center;justify-content:center;letter-spacing:6px}
.flow-line{position:absolute;left:25px;top:220px;width:3px;height:960px;background:var(--pink-soft)}
.step{position:absolute;left:50px;width:540px}
.step-head{display:flex;align-items:center;gap:10px;border-bottom:2px solid var(--pink-soft);padding-bottom:3px;width:100%}
.num{width:26px;height:26px;background:var(--pink);color:#fff;font-weight:700;font-size:17px;display:flex;align-items:center;justify-content:center}
.step-title{font-family:"M PLUS Rounded 1c",sans-serif;font-weight:800;font-size:23px;color:var(--rose)}
.step-body{font-size:12px;line-height:1.65;padding:7px 0 0 36px}
.step-body b{color:var(--rose);font-weight:700}
.phone{margin-top:6px;font-size:12px}
.phone strong{font-size:26px;color:#333;font-weight:700;margin-left:12px;letter-spacing:1px}
.zero{position:absolute;left:630px;top:505px;width:200px;height:132px;background:var(--pink);color:#fff;
  text-align:center;font-family:"M PLUS Rounded 1c",sans-serif;font-weight:800;padding-top:12px}
.zero .lead{font-size:34px;line-height:1.1}
.zero .amount{font-size:58px;line-height:1.1}
.zero .amount span{font-size:36px}
.person{position:absolute;right:0;top:820px;width:250px;height:380px;
  background:linear-gradient(180deg,#f6f2f2 0%,#e5dcdc 45%,#3a3436 100%)}
.bubble{position:absolute;width:100px;height:100px;border-radius:50%;background:var(--pink);color:#fff;
  display:flex;align-items:center;justify-content:center;text-align:center;font-weight:700;font-size:19px;line-height:1.25}
.b1{left:578px;top:860px}
.b2{left:578px;top:985px}
</style>
</head>
<body>
<div class="blossom" role="img" aria-label="淡いピンクの桜の花の写真"></div>
<h1 class="title">生活保護<small>の</small>ご葬儀</h1>
<div class="flow-label">流れ</div>
<div class="flow-line"></div>

<section class="step" style="top:140px">
  <div class="step-head"><span class="num">1</span><span class="step-title">ご臨終</span></div>
  <p class="step-body">生活保護受給者がお亡くなりになった場合、弊社にご連絡ください。<br>24時間体制でご対応致します。</p>
  <p class="step-body phone">お問い合せ先電話番号：<strong>0000-000-000</strong></p>
</section>

<section class="step" style="top:272px">
  <div class="step-head"><span class="num">2</span><span class="step-title">お迎え</span></div>
  <p class="step-body">お亡くなりになられた場所へ弊社担当者が、専用寝台車でお迎えにあがります。</p>
</section>

<section class="step" style="top:370px">
  <div class="step-head"><span class="num">3</span><span class="step-title">ご搬送・ご遺体安置</span></div>
  <p class="step-body">ご希望の場所にご搬送・ご安置致します。弊社のご遺体保管室でのお預かりも可能です。</p>
</section>

<section class="step" style="top:468px">
  <div class="step-head"><span class="num">4</span><span class="step-title">お打合せ</span></div>
  <p class="step-body"><b>①</b> お打合せ・火葬場予約を致します。<br>
  役所の福祉担当者と生活保護葬を行う旨を確認し、火葬場の予約や日程の調整を行います。<br>
  ご遺族様がいらっしゃらない場合も、弊社担当者がすべて代行致します。<br>
  <b>②</b> 死亡届提出<br>
  死亡診断書を添えて、役所へ死亡届を提出し、火葬許可証を受け取ります。</p>
</section>

<section class="step" style="top:655px">
  <div class="step-head"><span class="num">5</span><span class="step-title">ご出棺・火葬</span></div>
  <p class="step-body">火葬当日は、御遺族・お知り合いの方と一緒にお別れをしていただけます。<br>
  ご納棺、ご焼香も行っていただけます。<br>
  ※火葬場での待ち合わせの場合は、事前に弊社担当者にご相談ください。</p>
</section>

<section class="step" style="top:815px">
  <div class="step-head"><span class="num">6</span><span class="step-title">荼毘</span></div>
  <p class="step-body">故人様を火葬場にてお見送り致します。<br>控室でお待ちいただきます。（火葬時間は約1時間〜1時間30分）</p>
</section>

<section class="step" style="top:915px">
  <div class="step-head"><span class="num">7</span><span class="step-title">ご収骨</span></div>
  <p class="step-body">ご収骨をお手伝いさせていただきます。<br>
  ご遺骨は骨壺に納め、ご遺族様にお渡し致します。<br>
  ご遺族様がいらっしゃらない場合は、弊社にて供養・納骨の手配をお手伝い致します。</p>
</section>

<section class="step" style="top:1040px">
  <div class="step-head"><span class="num">8</span><span class="step-title">生活保護葬のご請求申請</span></div>
  <p class="step-body">葬祭扶助の申請は、弊社が役所へご請求の手続きを致します。<br>
  ご遺族様の費用のご負担はございませんので、ご安心ください。</p>
</section>

<div class="zero">
  <div class="lead">自己負担</div>
  <div class="amount">0<span>円</span></div>
</div>

<div class="person" role="img" aria-label="スーツ姿で案内する女性スタッフの写真"></div>
<div class="bubble b1">不安を<br>安心に</div>
<div class="bubble b2">疑問を<br>納得へ</div>
</body>
</html>
```